Bref créative
Stationery, etc. for a tax preparation company
looking for creative designs!
Professional
Gordon Pallister
4829 Brevard Court, Suite 100
Larkmoor, Ohio 43512
gordy@gordyvalmor.com
www.gptaxhelpers.com
We'd like something a little bit creative that stands out.
We'd like the back of the business card to be a lighter color so someone could write on it, if necessary.

```html
<!DOCTYPE html>
<html lang="en">
<head>
<meta charset="utf-8">
<title>Northfield Returns – Business Card</title>
<link rel="stylesheet" href="https://fonts.googleapis.com/css2?family=Cinzel:wght@400&display=swap">
<style>
  :root {
    --plum: #5e2a78;
    --plum-light: #8a4fa6;
    --plum-dark: #3f1a52;
    --paper: #ffffff;
    --silver: #c9c6cc;
    --backdrop: #ece9ee;
    --ink-light: #ffffff;
  }
  * { margin: 0; padding: 0; box-sizing: border-box; }
  html, body {
    width: 1200px; height: 914px; overflow: hidden;
    background: var(--backdrop);
  }
  .card {
    position: absolute; left: 80px; top: 157px;
    width: 1040px; height: 600px;
    background: var(--paper);
    box-shadow: 0 10px 30px rgba(0,0,0,.18);
    overflow: hidden;
    font-family: "Cinzel", serif;
  }
  .card-field { position: absolute; inset: 0; }
  .holder-name {
    position: absolute; left: 48px; top: 40px;
    color: var(--ink-light); font-size: 24px; letter-spacing: 1px;
  }
  .contact-list {
    position: absolute; left: 48px; top: 300px;
    list-style: none; color: var(--ink-light);
    font-size: 16px; line-height: 1.25; letter-spacing: .5px;
  }
  .contact-list li { display: flex; align-items: flex-start; gap: 12px; margin-bottom: 6px; }
  .contact-icon { flex: none; width: 20px; height: 20px; margin-top: 1px; }
  .brand {
    position: absolute; left: 580px; top: 330px; width: 420px;
    display: flex; align-items: center; justify-content: center; gap: 16px;
    color: var(--plum); font-size: 36px; font-weight: 400; letter-spacing: 1px;
    white-space: nowrap;
  }
  .brand-dot {
    flex: none; width: 26px; height: 26px;
    border-radius: 50%; background: var(--plum);
  }
</style>
</head>
<body>
  <div class="card">
    <svg class="card-field" width="1040" height="600" viewBox="0 0 1040 600" aria-hidden="true">
      <defs>
        <radialGradient id="plumGlow" cx="0.35" cy="0.25" r="0.8">
          <stop offset="0" stop-color="#8a4fa6"/>
          <stop offset="1" stop-color="#3f1a52"/>
        </radialGradient>
      </defs>
      <path d="M0 0 H640 C560 110 520 210 470 320 C420 440 360 540 300 600 H0 Z" fill="url(#plumGlow)"/>
      <path d="M660 0 C580 120 540 220 490 330 C445 440 385 540 325 600" fill="none" stroke="#c9c6cc" stroke-width="6"/>
    </svg>

    <div class="holder-name">Gordon Pallister</div>

    <ul class="contact-list">
      <li>
        <svg class="contact-icon" viewBox="0 0 22 22"><circle cx="11" cy="11" r="11" fill="#fff"/><path d="M11 5a4 4 0 0 0-4 4c0 3 4 8 4 8s4-5 4-8a4 4 0 0 0-4-4zm0 5.5a1.5 1.5 0 1 1 0-3 1.5 1.5 0 0 1 0 3z" fill="#5e2a78"/></svg>
        <span>4829 Brevard Court, Unit 7<br>Larkmoor, Ohio 43512</span>
      </li>
      <li>
        <svg class="contact-icon" viewBox="0 0 22 22"><circle cx="11" cy="11" r="11" fill="#fff"/><path d="M7 6l2.5-.5 1.2 3-1.5 1a6 6 0 0 0 3 3l1-1.5 3 1.2L15.7 15C11 15.5 6.5 11 7 6z" fill="#5e2a78"/></svg>
        <span>612-555-0173</span>
      </li>
      <li>
        <svg class="contact-icon" viewBox="0 0 22 22"><circle cx="11" cy="11" r="11" fill="#fff"/><rect x="6" y="8" width="10" height="7" fill="#5e2a78"/><rect x="8" y="5" width="6" height="3" fill="#5e2a78"/></svg>
        <span>612-555-0188</span>
      </li>
      <li>
        <svg class="contact-icon" viewBox="0 0 22 22"><circle cx="11" cy="11" r="11" fill="#fff"/><circle cx="11" cy="11" r="5" fill="#5e2a78"/></svg>
        <span>brivonsa482</span>
      </li>
      <li>
        <svg class="contact-icon" viewBox="0 0 22 22"><circle cx="11" cy="11" r="11" fill="#fff"/><rect x="5.5" y="7" width="11" height="8" fill="#5e2a78"/><path d="M5.5 7l5.5 4.5L16.5 7" fill="none" stroke="#fff" stroke-width="1.2"/></svg>
        <span>gordy@gordyvalmor.com</span>
      </li>
      <li>
        <svg class="contact-icon" viewBox="0 0 22 22"><circle cx="11" cy="11" r="11" fill="#fff"/><circle cx="11" cy="11" r="5.5" fill="none" stroke="#5e2a78" stroke-width="1.4"/><path d="M5.5 11h11M11 5.5c-3 3-3 8 0 11M11 5.5c3 3 3 8 0 11" fill="none" stroke="#5e2a78" stroke-width="1.1"/></svg>
        <span>www.gptaxhelpers.com</span>
      </li>
    </ul>

    <div class="brand">
      <span class="brand-dot"></span>
      <span class="brand-name">Northfield Returns</span>
    </div>
  </div>
</body>
</html>
```